Verdant Harbor wants proposals to design and develop a new website, tying together the visuals and branding message initiated with the package design. The goals of this website will be to provide an excellent user experience, to make the website a vital source of information that
will be indexed by the search engines and to facilitate and encourage consumer confidence.
The design and function of the website will be instrumental in generating knowledge of and trust in the product line.

Our current website Verdantharbor.com is an informational and transactional website. We are looking to completely overhaul the informational side. The products we sell are unique combinations of Ayurvedic herbal supplements. They are very effective and of a superior quality. However, the current website in all fairness is "blah". The site should be professional, visually enticing, reliable and efficient, compatible with virtually any computer that connects to it and makes for a first rate impression to our customers.

We want a website which will relay to the customer the effectiveness and superior quality of our products. We want the site to engage the customer. The website needs to be an experience and to connect to the customer emotionally. It is a tall order but it is what we need to deliver our message. A majority of the traffic comes from people already interested in a particular condition that our product is used for. Our goal is for the customer to be convinced that the solution is our product which it is in most cases.

The design should be able to handle fields that are currently on the site, like article links to external sites, video clips on products, specials, etc. The site is currently powered on the back end by .NET 4.0 with MVC architecture and this we hope to continue. Also, the text to HTML has to be a very good ratio.

The current pages are very well indexed and search engine optimized and that concept has to be preserved. At this point, we do not want to build a separate mobile version so flash is not an option.
Updates

Pleas come up with original ideas and not just refreshing currently what I have.

Pictures used need to be realistic.  Faces are ok to use but not necessary.  The picture/graphic needs to communicate effectiveness and high quality of products.  Also the overall look and feel needs to be addressed.  Please don't take existing part of current website and paste onto new one.  

We are disappointed in the overall designs received.  They all look like cut and paste websites. One that we did like was showing herbs held in the hand.  We are not opposed to faces being shown but it has to look "real".  Also the space below the picture needs to be developed more.  We are not focusing on transactions on this website although a link will be provided for those interested in purchasing.

After reviewing all designs, it seems showing herbs/flowers/nature is a better way to go.  The picture of women makes our company look more like a spa which is not our intent.  

Target Market(s)

USA, Canada, Western European customers; 60% Females, 40% male; 35 plus age group

Industry/Entity Type

Architecture

Requirements
Must have
• Good Text to Html ratio. Should be SEO compatible. Feel good and engaging audience.
Should not have
• Must be mobile compatible and should not be flash based.

```html
<!DOCTYPE html>
<html lang="en">
<head>
<meta charset="utf-8">
<title>Verdant Harbor – Herbal Natural Supplements</title>
<link rel="stylesheet" href="https://fonts.googleapis.com/css2?family=Jost:wght@400;500&family=PT+Sans:wght@400;700&family=Arimo:ital,wght@0,400;0,700;1,400&display=swap">
<style>
:root{
  --green-dark:#376b06;
  --green-text:#2f5d05;
  --lime:#8fc31f;
  --lime-mid:#6fa30f;
  --yellow:#f5d800;
  --orange:#c77a00;
  --grey-text:#999;
  --grey-dark:#555;
  --panel:#f6f6f6;
  --line:#dcdcdc;
  --white:#fff;
}
*{box-sizing:border-box;margin:0;padding:0}
html,body{width:1200px;height:1000px;overflow:hidden;background:var(--white)}
body{position:relative;font-family:Arimo,Arial,sans-serif;color:var(--grey-dark)}
.abs{position:absolute}
a{color:inherit;text-decoration:none}

/* header */
.header-pattern{left:230px;top:5px;width:800px;height:116px;border-radius:8px;
  background:linear-gradient(90deg,rgba(235,242,215,.9),rgba(245,248,232,.6) 50%,rgba(236,243,218,.9))}
.brand{left:250px;top:58px;display:flex;align-items:center;gap:10px;
  font-family:"PT Sans",sans-serif;font-weight:700;font-size:38px;color:#1f2a12;letter-spacing:.5px}
.brand-dot{width:22px;height:22px;border-radius:50%;background:var(--lime)}
.top-links{right:167px;top:9px;font-size:11px;font-weight:700;color:var(--green-text)}

/* nav */
.main-nav{left:230px;top:156px;width:803px;height:44px;border-radius:8px;background:var(--green-dark)}
.main-nav a{position:absolute;top:13px;font-family:Jost,sans-serif;font-weight:500;font-size:14.5px;
  color:var(--white);text-transform:uppercase;letter-spacing:.2px}
.main-nav a.active{color:var(--yellow)}
.main-nav .sep{position:absolute;top:14px;width:1px;height:16px;background:var(--white)}

/* sidebar */
.sidebar{left:230px;top:220px;width:193px;height:598px;background:var(--green-dark)}
.promo-title{left:245px;top:262px;font-family:"PT Sans",sans-serif;font-size:21px;color:var(--yellow)}
.promo-sub{left:245px;top:296px;font-family:"PT Sans",sans-serif;font-size:15px;color:var(--white)}
.search{left:243px;top:321px;width:167px;height:32px;display:flex}
.search-field{flex:1;background:var(--white);font-size:13px;color:#c8c8c8;padding:8px 10px}
.search-btn{width:30px;background:var(--lime);color:var(--white);font-family:"PT Sans",sans-serif;font-size:12px;font-weight:700;display:flex;align-items:center;justify-content:center}
.video{left:245px;top:375px;width:165px;height:133px;background:#111}
.video-frame{position:absolute;left:0;top:18px;width:165px;height:97px;
  background:linear-gradient(120deg,#5e6b52,#8a8677 45%,#3f4536)}
.video-title{position:absolute;left:8px;top:4px;font-size:10px;color:var(--white)}
.video-play{position:absolute;left:66px;top:55px;width:34px;height:23px;border-radius:5px;background:rgba(20,20,20,.85)}
.video-play::after{content:"";position:absolute;left:13px;top:6px;border-left:10px solid var(--white);border-top:6px solid transparent;border-bottom:6px solid transparent}
.side-heading{font-family:"PT Sans",sans-serif;font-size:15px;color:var(--yellow)}
.therapy-list{left:255px;top:666px;list-style:none}
.therapy-list li{font-size:11px;color:var(--white);height:21.3px;display:flex;align-items:center;gap:3px}
.therapy-list li::before{content:"";border-left:7px solid var(--white);border-top:5px solid transparent;border-bottom:5px solid transparent}

.follow{left:230px;top:808px;width:193px;height:80px;background:var(--panel);border:1px solid #e6e6e6}
.follow h3{position:absolute;left:12px;top:10px;font-family:"PT Sans",sans-serif;font-weight:400;font-size:16px;color:#777}
.social{position:absolute;top:36px;width:25px;height:25px;border-radius:3px}

/* tab band */
.tab-band{left:423px;top:220px}

/* content */
.intro-title{left:432px;top:264px;font-family:"PT Sans",sans-serif;font-size:15px;color:var(--green-text)}
.intro-text{left:432px;top:295px;width:424px;font-size:12px;line-height:19px;color:var(--grey-text);text-align:justify}
.featured-title{left:432px;top:373px;font-size:15px;font-weight:700;color:var(--orange)}
.product{width:194px;height:88px;border-bottom:1px solid var(--line)}
.product h4{position:absolute;left:0;top:0;font-size:12px;font-weight:700;color:var(--orange)}
.product-img{position:absolute;left:0;top:18px;width:52px;height:42px;border-radius:40%;
  background:radial-gradient(circle at 50% 50%,#d9b25a,#c45a2a 55%,rgba(143,195,31,.6) 75%,transparent 78%)}
.product-img.mortar{background:radial-gradient(circle at 50% 60%,#e8e8e0,#b5b5a8 55%,rgba(90,140,40,.5) 72%,transparent 75%)}
.product p{position:absolute;left:57px;top:14px;width:140px;font-size:10.5px;line-height:14.5px;color:var(--grey-text)}
.product .more{position:absolute;right:0;top:72px;font-size:9px;font-weight:700;color:var(--green-text)}

.services{left:863px;top:257px;width:171px;height:312px;background:#f9f9f9;border:1px solid #ececec;border-radius:6px}
.services h3{position:absolute;left:13px;top:7px;font-family:"PT Sans",sans-serif;font-weight:400;font-size:15px;color:var(--green-text)}
.service{position:absolute;left:10px;width:155px}
.service-num{position:absolute;left:0;top:0;width:24px;height:24px;border-radius:50%;background:var(--green-dark);color:var(--white);font-family:"PT Sans",sans-serif;font-weight:700;font-style:italic;font-size:15px;display:flex;align-items:center;justify-content:center}
.service h4{position:absolute;left:29px;top:-1px;font-size:11.5px;font-weight:700;color:#444;white-space:nowrap}
.service p{position:absolute;left:30px;top:16px;width:125px;font-size:10.5px;line-height:14.5px;color:#444}

.testimonial-title{left:871px;top:581px;font-family:"PT Sans",sans-serif;font-weight:700;font-size:16px;color:var(--green-text)}
.testimonial-text{left:871px;top:607px;width:165px;font-size:10.5px;line-height:15px;font-style:italic;color:var(--grey-dark)}
.author{font-size:10.5px;font-weight:700;color:var(--orange)}

.speak{left:432px;top:756px;width:420px;height:132px;background:var(--panel);border:1px solid #e6e6e6;border-radius:8px}
.speak h3{position:absolute;left:17px;top:18px;font-family:"PT Sans",sans-serif;font-weight:400;font-size:16px;color:var(--green-text)}
.speak-icon{position:absolute;left:16px;top:48px}
.speak p{position:absolute;left:56px;top:42px;width:354px;font-size:10.5px;line-height:14.5px;color:var(--grey-text)}
.speak .author{position:absolute;right:13px;top:100px}

.newsletter{left:870px;top:758px;width:164px;height:130px;background:var(--lime-mid)}
.newsletter h3{height:28px;background:var(--green-dark);padding:6px 9px;font-family:Arimo,sans-serif;font-weight:400;font-size:13px;color:var(--yellow)}
.newsletter p{position:absolute;left:10px;top:40px;font-size:10px;color:var(--white)}
.newsletter-field{position:absolute;left:11px;top:62px;width:146px;height:18px;background:#dff0c4}
.newsletter-btn{position:absolute;left:11px;top:91px;width:72px;height:21px;border-radius:11px;background:var(--lime);border:1px solid #b5dc6a;font-size:9.5px;font-weight:700;color:var(--white);display:flex;align-items:center;justify-content:center}

/* footer */
.footer-line{left:230px;top:904px;width:804px;height:7px;background:var(--lime)}
.site-footer{left:188px;top:910px;width:884px;height:90px;background:var(--green-dark);text-align:center}
.footer-links{margin-top:34px;font-size:11px;color:var(--white)}
.footer-links a{margin:0 4px}
.copyright{margin-top:9px;font-size:9.5px;color:var(--yellow)}
</style>
</head>
<body>

<header>
  <div class="abs header-pattern" role="img" aria-label="Soft pale green mosaic of rounded squares behind the header"></div>
  <div class="abs brand"><span class="brand-dot"></span>Verdant Harbor</div>
  <div class="abs top-links">Welcome Guest | <a href="#">Home</a> | <a href="#">Bookmark</a> | <a href="#">Sitemap</a> | <a href="#">Contact Us</a></div>
  <nav class="abs main-nav">
    <a class="active" href="#" style="left:24px">Suppliments</a><span class="sep" style="left:112px"></span>
    <a href="#" style="left:135px">Skin Care</a><span class="sep" style="left:224px"></span>
    <a href="#" style="left:248px">Our Retailers</a><span class="sep" style="left:361px"></span>
    <a href="#" style="left:384px">Articals</a><span class="sep" style="left:458px"></span>
    <a href="#" style="left:483px">About Us</a><span class="sep" style="left:577px"></span>
    <a href="#" style="left:603px">Register/Enquiry</a>
  </nav>
</header>

<aside>
  <div class="abs sidebar"></div>
  <div class="abs promo-title">Free Shipping</div>
  <div class="abs promo-sub">on Order of $20 or more</div>
  <div class="abs search"><div class="search-field">Search</div><div class="search-btn">Go</div></div>
  <div class="abs video">
    <div class="video-title">Verdant Harbor USA</div>
    <div class="video-frame" role="img" aria-label="Product video still of a presenter in a bright room"></div>
    <div class="video-play"></div>
  </div>
  <div class="abs side-heading" style="left:243px;top:527px">Secure Payments</div>
  <div class="abs side-heading" style="left:243px;top:637px">Alternative Therapies</div>
  <ul class="abs therapy-list">
    <li>Ayurwed Herbs</li><li>Ayurwed Herbs</li><li>Ayurwed Herbs</li><li>Ayurwed Herbs</li>
  </ul>
  <div class="abs follow">
    <h3>Follow Us</h3>
    <span class="social" style="left:12px;background:#3b5998"></span>
    <span class="social" style="left:44px;background:#5fb8e8"></span>
    <span class="social" style="left:78px;background:#9a9a9a"></span>
    <span class="social" style="left:112px;background:#c4302b"></span>
  </div>
</aside>

<svg class="abs tab-band" width="612" height="27" viewBox="0 0 612 27" aria-hidden="true">
  <polygon points="0,0 17,18 0,18" fill="#6fa30f"/>
  <rect x="0" y="18" width="611" height="8" fill="#8fc31f"/>
</svg>

<main>
  <h1 class="abs intro-title">Herbal Natural Supplements: Authentic Formulas</h1>
  <p class="abs intro-text">All of our Herbal Natural Supplements and Skincare Products are made using authentic ancient time tested formulations and have an excellent track record.</p>
  <h2 class="abs featured-title">Featured Products</h2>

  <article class="abs product" style="left:433px;top:407px;height:94px">
    <h4>Stress Supplements</h4><div class="product-img mortar" role="img" aria-label="Mortar and pestle with fresh herbs"></div>
    <p>Ayurvedic hospital with resident Ayurvedic physicians, Therapists, Health Centre, Dispensary, Yoga &amp; Meditation Centre</p><span class="more">+more</span>
  </article>
  <article class="abs product" style="left:648px;top:407px;width:204px;height:94px">
    <h4>Skin Care</h4><div class="product-img" role="img" aria-label="Dried herbs and spices"></div>
    <p style="left:63px">Ayurvedic hospital with resident Ayurvedic physicians, Therapists, Health Centre, Dispensary, Yoga &amp; Meditation Centre</p><span class="more" style="top:78px">+more</span>
  </article>
  <article class="abs product" style="left:433px;top:524px;height:93px">
    <h4>Herbs that Cure</h4><div class="product-img" role="img" aria-label="Dried herbs and spices"></div>
    <p style="top:18px">Ayurvedic hospital with resident Ayurvedic physicians, Therapists, Health Centre, Dispensary, Yoga &amp; Meditation Centre</p><span class="more" style="top:76px">+more</span>
  </article>
  <article class="abs product" style="left:659px;top:524px;height:93px">
    <h4>Packages</h4><div class="product-img" role="img" aria-label="Dried herbs and spices"></div>
    <p style="top:18px">Ayurvedic hospital with resident Ayurvedic physicians, Therapists, Health Centre, Dispensary, Yoga &amp; Meditation Centre</p><span class="more" style="top:76px">+ more</span>
  </article>
  <article class="abs product" style="left:433px;top:634px;height:94px">
    <h4>Packages</h4><div class="product-img" role="img" aria-label="Dried herbs and spices"></div>
    <p style="top:18px">Ayurvedic hospital with resident Ayurvedic physicians, Therapists, Health Centre, Dispensary, Yoga &amp; Meditation Centre</p><span class="more" style="top:77px">+ more</span>
  </article>
  <article class="abs product" style="left:659px;top:634px;height:94px">
    <h4>Packages</h4><div class="product-img" role="img" aria-label="Dried herbs and spices"></div>
    <p style="top:18px">Ayurvedic hospital with resident Ayurvedic physicians, Therapists, Health Centre, Dispensary, Yoga &amp; Meditation Centre</p><span class="more" style="top:78px">+ more</span>
  </article>

  <section class="abs speak">
    <h3>Customer Speak</h3>
    <svg class="speak-icon" width="34" height="34" viewBox="0 0 34 34" aria-hidden="true">
      <path d="M0 0h20v14H8l-5 5v-5H0z" fill="#a9a9a9"/>
      <path d="M13 17h21v13h-3v5l-5-5H13z" fill="#a9a9a9"/>
    </svg>
    <p>There is no parallel system as far as technology is concerned. However, in the field of Medical Sciences, there is a system of Indian Medicine parallel to that of Modern system of Medicine Indian Medicine parallel to that of Modern system of Medicine</p>
    <span class="author">-Anil Deshmane</span>
  </section>
</main>

<aside>
  <section class="abs services">
    <h3>Services</h3>
    <div class="service" style="top:46px"><span class="service-num">1</span><h4>This is a test Program</h4><p>I'm designing a webpage, and the concept is a television set that plays</p></div>
    <div class="service" style="top:121px"><span class="service-num">2</span><h4>This is a test Program</h4><p>I'm designing a webpage, and the concept is a television set that plays</p></div>
    <div class="service" style="top:192px"><span class="service-num">3</span><h4>This is a test Program</h4><p>I'm designing a webpage, and the concept is a television set that plays</p></div>
  </section>
  <h3 class="abs testimonial-title">Testimonial</h3>
  <p class="abs testimonial-text">I'm designing a webpage, and the concept is a television set that plays I'm designing a webpage, and the concept is a television set that plays</p>
  <span class="abs author" style="left:942px;top:679px">-Anil Deshmane</span>

  <section class="abs newsletter">
    <h3>Newsletter</h3>
    <p>Sign up for our newsletter</p>
    <div class="newsletter-field"></div>
    <div class="newsletter-btn">Subscribe</div>
  </section>
</aside>

<div class="abs footer-line"></div>
<footer class="abs site-footer">
  <div class="footer-links"><a href="#">Home</a> | <a href="#">Help Customer Support</a> | <a href="#">Returns</a> | <a href="#">Terms of Uses</a> | <a href="#">FAQ</a> | <a href="#"><b>Privacy Policy</b></a></div>
  <div class="copyright">© 2010 Verdantharbor.com. All Rights Reserved.</div>
</footer>

</body>
</html>
```